Flyer-Design für Kanutouristiker (Kanu Vermietung) Folgeaufträge!!
Zielgruppe
Wir veranstalten Kanu - und Erlebnistouren. Vermieten Kanus, Schlauchboote (Rafts), SUP (Stand up Paddling) und Fahrräder.
Für Gruppen, Betriebe, Schulklassen, Vereine, Familien, Junggesellenabschiede, Geburtstage usw.
Aufgabenstellung
Wir möchten einen ansprechenden Flyer erstellen lassen, der Lust auf unsere Angebote machen soll.
Hier handelt es sich um einen DIN lang (A4) Wickelfalz Falter (6 Seiter)
Mit unseren Angeboten. Beispielbilder sind im Anhang mithochgeladen. Es können weitere geliefert werden- oder Sie sehen sich einmal auf unserer Webseite um.
Wenig Text- lassen Sie die Bilder sprechen!!
Der Flyer soll lust auf eine Tour bei uns machen!
Der Flyer soll natürlich wirken.
Unsere CI wird schon durch unser Logo mitgegeben- es müssen nicht unbeding gr. Flächen mit unseren Farben gefüllt werden!!
Uns sprechen filigrane, künstlerische Designs an. Aber bitte die natürlichkeit nicht aus den Augen verlieren. Wir sind OUTDOORveranstalter- unsere Aktionen finden in der Natur statt!
Eine Variante, die ich aus zahlreichen Designs erarbeitet habe:
Nutzen Sie ein grosses Bild als Header (Kopfzeile) das auch z.B. im Orangeton (Logofarbe) überzeichnet - oder auch nur weiss (milchig) verändert sein darf.
Hierauf einen geeigneten Sinnspruch (Überschrift) z.B. "..mehr als nur ein Abenteuer"
der passend sein muss.
Etwas Poetisches vielleicht.... kurz und prägnant. (Natur, ökologie, Wasser, reisen...).
Bilder groß und darauf überlagert kleinere eingefasst in Rahmen.
Zum Textinhalt
Titelseite:
was machen wir?
Paddel- & Radtouren im Weser-Leinebergland, tolles Bild und unser Logo
evtl. noch für wen geeignet?
Schulklassen, Betriebe, Vereine, Familien, Junggesellenabschiede etc.
Innenseite(n):
Bilder, Bilder, Bilder (vielleicht gr. Hintergrundbild, dann kleine Bilder drauf mit passender Überschrift: z.B. Abenteuer im Tivorunde, Stand up paddling, Teambuilding Flossbau, Radverleih, Strudel & Speiche, usw.
Rückseite:
Unsere Kontaktdaten
Firmenname
Webseite
Mailadresse
Hausanschrift
plaudernetz
QR Code
LOGO
Toll wäre ein..

```html
<!DOCTYPE html>
<html lang="de">
<head>
<meta charset="utf-8">
<title>Auenpaddel – Faltblatt</title>
<link href="https://fonts.googleapis.com/css2?family=Kaushan+Script&family=Raleway:wght@400;600&family=Open+Sans:wght@600;700&display=swap" rel="stylesheet">
<style>
  :root {
    --stage: #444444;
    --red: #c0141f;
    --orange: #f39200;
    --white: #ffffff;
    --text: #3a3a3a;
  }
  * { box-sizing: border-box; margin: 0; padding: 0; }
  html, body { width: 804px; height: 1200px; overflow: hidden; }
  body { background: var(--stage); position: relative; font-family: "Raleway", sans-serif; }

  .sheet-row { position: absolute; left: 22.5px; width: 759.5px; height: 531px; display: flex; }
  .sheet-row--outside { top: 54px; }
  .sheet-row--inside { top: 601px; }

  .panel { position: relative; width: 253px; height: 531px; overflow: hidden; background: var(--white); }
  .panel:nth-child(2) { width: 253.5px; }

  .photo { position: absolute; left: 0; top: 0; width: 100%; height: 370px; }
  .photo--kayak-green {
    background:
      radial-gradient(ellipse 70% 30% at 70% 25%, rgba(60,90,45,.9), transparent 70%),
      radial-gradient(ellipse 80% 45% at 75% 75%, #55c84a, transparent 75%),
      linear-gradient(165deg, #b9d2ea 0%, #8fb0cf 14%, #4d7a3c 24%, #7a8a90 38%, #6c7c82 48%, #48b843 62%, #3aa83a 100%);
  }
  .photo--canoe-castle {
    background:
      radial-gradient(ellipse 35% 60% at 88% 30%, rgba(170,130,100,.85), transparent 70%),
      radial-gradient(ellipse 90% 25% at 50% 88%, #d42a36, transparent 80%),
      linear-gradient(180deg, #4f9de8 0%, #8dbbe8 28%, #5e9a3c 42%, #3f7d2a 62%, #b8343c 80%, #d9404a 100%);
  }
  .photo--tipi-camp {
    background:
      radial-gradient(ellipse 45% 35% at 28% 55%, #ece4cc, transparent 72%),
      radial-gradient(ellipse 40% 15% at 75% 45%, #f0f0ee, transparent 75%),
      linear-gradient(180deg, #8293ab 0%, #9aa8bb 20%, #3e5b38 34%, #587a42 50%, #5b9330 68%, #4a7d22 100%);
  }
  .photo--raft-youth {
    background:
      radial-gradient(ellipse 80% 25% at 55% 60%, #e02a2a, transparent 75%),
      radial-gradient(ellipse 60% 30% at 40% 15%, #8cc84c, transparent 75%),
      linear-gradient(180deg, #3c7a24 0%, #6fae3c 30%, #b84040 52%, #c83030 64%, #5d6a6a 82%, #3b4a4a 100%);
  }
  .photo--raft-cheer {
    position: absolute; left: 0; top: 120px; width: 100%; height: 411px;
    background:
      radial-gradient(ellipse 70% 25% at 55% 30%, rgba(200,194,178,.8), transparent 75%),
      radial-gradient(ellipse 90% 30% at 60% 58%, #cf3a3a, transparent 75%),
      linear-gradient(180deg, #4d7a36 0%, #8fb85a 22%, #c8c2b2 34%, #b84444 52%, #2b2b2b 74%, #5a1c1c 90%, #7a2424 100%);
  }

  .wave { position: absolute; left: 0; top: 0; width: 100%; height: 100%; }

  .offer { position: absolute; left: 25px; right: 18px; top: 372px; }
  .offer__title { font-family: "Kaushan Script", cursive; color: var(--red); font-size: 28px; line-height: 1.1; letter-spacing: -0.5px; }
  .offer__tagline { font-family: "Kaushan Script", cursive; color: var(--orange); font-size: 12px; line-height: 1.3; margin-bottom: 8px; }
  .offer__text { color: var(--text); font-size: 10.3px; line-height: 13px; }
  .offer__text + .offer__text { margin-top: 4px; }

  .panel--contact { background: var(--red); overflow: visible; }
  .contact-brand { position: absolute; top: 200px; left: 0; width: 100%; display: flex; justify-content: center; align-items: center; gap: 6px; }
  .brand-dot { width: 14px; height: 14px; border-radius: 50%; background: var(--white); }
  .brand-name { font-family: "Raleway", sans-serif; font-weight: 600; font-size: 15px; color: var(--white); }
  .contact { position: absolute; top: 260px; left: 0; width: 100%; text-align: center; color: var(--white); font-family: "Open Sans", sans-serif; }
  .contact__company { font-weight: 700; font-size: 7.5px; line-height: 10px; letter-spacing: 0.4px; margin-bottom: 6px; }
  .contact__line { font-weight: 600; font-size: 7px; line-height: 10px; }
  .contact__gap { height: 5px; }

  .top-wave { position: absolute; left: 253px; top: 0; width: 506.5px; height: 160px; pointer-events: none; z-index: 1; }

  .cover-brand { position: absolute; top: 54px; right: 32px; display: flex; align-items: center; gap: 7px; z-index: 2; }
  .cover-brand .brand-dot { background: var(--orange); width: 20px; height: 20px; }
  .cover-brand .brand-name { color: var(--orange); font-size: 20px; }

  .headline { position: absolute; left: 82px; top: 424px; font-family: "Open Sans", sans-serif; font-weight: 700; line-height: 1; letter-spacing: 1px; }
  .headline__line { display: block; color: var(--orange); font-size: 27px; }
  .headline__line--accent { color: var(--red); font-size: 35px; margin: 0 0 1px; }
</style>
</head>
<body>

<section class="sheet-row sheet-row--outside">
  <article class="panel panel--offer">
    <div class="photo photo--kayak-green" role="img" aria-label="Foto: grünes Kajak mit Gepäcknetz im Vordergrund, dahinter ein rotes Kanu mit Paddlerinnen auf dem Fluss vor bewaldetem Hang"></div>
    <svg class="wave" viewBox="0 0 253 531" aria-hidden="true">
      <path d="M0,288 C30,282 45,292 24,302 C2,314 25,345 120,356 C170,361 215,362 253,362 L253,531 L0,531 Z" fill="#ffffff"/>
      <path d="M0,288 C30,282 45,292 24,302 C2,314 25,345 120,356 C170,361 215,362 253,362" fill="none" stroke="#f39200" stroke-width="7"/>
    </svg>
    <div class="offer">
      <h2 class="offer__title">Radtouren</h2>
      <p class="offer__tagline">Paddeln im Stehen.</p>
      <p class="offer__text">Bei uns bekommen Sie hochwertige Miet­fahrräder für Ihren Urlaub oder Ihre kleine Tour im Weser-Leinebergland.</p>
      <p class="offer__text">Ein leichter Alurahmen, gefederte Sattel­stütze und eine 7- Gang Nabenschaltung zeichnen unsere Räder aus.</p>
    </div>
  </article>

  <article class="panel panel--contact">
    <div class="contact-brand">
      <span class="brand-dot"></span>
      <span class="brand-name">auenpaddel.de</span>
    </div>
    <div class="contact">
      <p class="contact__company">AUENPADDEL<br>KANUTOURISTIK</p>
      <p class="contact__line">Helga Sonnfeld</p>
      <p class="contact__line">12345 Lindenau (Am Flussufer)</p>
      <div class="contact__gap"></div>
      <p class="contact__line">Tel.:&nbsp;&nbsp; 0 12 34 - 56 78 90</p>
      <p class="contact__line">Mobil: 0 17 00 - 12 34 567</p>
    </div>
  </article>

  <article class="panel panel--cover">
    <div class="photo--raft-cheer" role="img" aria-label="Foto: jubelnde Gruppe in Schwimmwesten reckt Paddel in einem roten Schlauchboot auf dem Fluss"></div>
    <h1 class="headline">
      <span class="headline__line">AUF DEM</span>
      <span class="headline__line headline__line--accent">WASSER</span>
      <span class="headline__line">ZU HAUSE.</span>
    </h1>
  </article>

  <svg class="top-wave" viewBox="0 0 506.5 160" aria-hidden="true">
    <path d="M0,0 H506.5 V126 C420,122 320,116 220,100 C130,86 62,78 56,58 C50,36 95,30 126,22 C132,16 100,14 0,16 Z" fill="#ffffff"/>
    <path d="M56,58 C62,82 130,96 220,110 C320,126 420,140 506.5,152 V126 C420,122 320,116 220,100 C130,86 62,78 56,58 Z" fill="#f39200"/>
    <path d="M0,16 C100,14 132,16 126,22 C95,30 50,36 56,58" fill="none" stroke="#f39200" stroke-width="6"/>
  </svg>

  <div class="cover-brand">
    <span class="brand-dot"></span>
    <span class="brand-name">auenpaddel.de</span>
  </div>
</section>

<section class="sheet-row sheet-row--inside">
  <article class="panel panel--offer">
    <div class="photo photo--canoe-castle" role="img" aria-label="Foto: vier Paddlerinnen in einem roten Kanu vor grünem Ufer und alter Burgmauer"></div>
    <svg class="wave" viewBox="0 0 253 531" aria-hidden="true">
      <path d="M0,288 C30,282 45,292 24,302 C2,314 25,345 120,356 C170,361 215,362 253,362 L253,531 L0,531 Z" fill="#ffffff"/>
      <path d="M0,288 C30,282 45,292 24,302 C2,314 25,345 120,356 C170,361 215,362 253,362" fill="none" stroke="#f39200" stroke-width="7"/>
    </svg>
    <div class="offer">
      <h2 class="offer__title">Kanutouren</h2>
      <p class="offer__tagline">Natur pur im Weser- und Leinebergland</p>
      <p class="offer__text">Genießen Sie die Orte aus einer anderen Perspektive. Erkunden Sie die Landschaft, erleben Sie wunderbare Flüsse und genießen Sie ein einmaliges Erlebnis. Die große Weser, die wilde Emmer oder die kleine Nethe - jeder Fluss garantiert einen hohen Funfactor.</p>
    </div>
  </article>

  <article class="panel panel--offer">
    <div class="photo photo--tipi-camp" role="img" aria-label="Foto: Zeltlager mit hellen Tipis auf einer Wiese, Gruppe an einem Biertisch vor bewaldeten Hügeln"></div>
    <svg class="wave" viewBox="0 0 253 531" aria-hidden="true">
      <path d="M0,288 C30,282 45,292 24,302 C2,314 25,345 120,356 C170,361 215,362 253,362 L253,531 L0,531 Z" fill="#ffffff"/>
      <path d="M0,288 C30,282 45,292 24,302 C2,314 25,345 120,356 C170,361 215,362 253,362" fill="none" stroke="#f39200" stroke-width="7"/>
    </svg>
    <div class="offer">
      <h2 class="offer__title">Schlauchboote</h2>
      <p class="offer__tagline">... Kentern ausgeschlossen!</p>
      <p class="offer__text">Ab sofort bieten wir tolle Touren auf der Weser, sowie der Leine in Raftboten an. In diesen Booten finden bis zu 12 Personen Platz. Eine Tour mit unseren Tivorunden ist eine tolle Alternative um auch „alle“ mit ins Boot zu bekommen. Einfache Handhabung und bequeme Sitzposition sind garantiert.</p>
    </div>
  </article>

  <article class="panel panel--offer">
    <div class="photo photo--raft-youth" role="img" aria-label="Foto: Jugendliche in Schwimmwesten paddeln in einem roten Schlauchboot unter grünen Bäumen"></div>
    <svg class="wave" viewBox="0 0 253 531" aria-hidden="true">
      <path d="M0,288 C30,282 45,292 24,302 C2,314 25,345 120,356 C170,361 215,362 253,362 L253,531 L0,531 Z" fill="#ffffff"/>
      <path d="M0,288 C30,282 45,292 24,302 C2,314 25,345 120,356 C170,361 215,362 253,362" fill="none" stroke="#f39200" stroke-width="7"/>
    </svg>
    <div class="offer">
      <h2 class="offer__title">Stand up Paddeling</h2>
      <p class="offer__tagline">Paddeln im Stehen.</p>
      <p class="offer__text">Egal ob Sie lieber ruhig paddeln möchten - zum Entspannen, sich einer Fitnesseinheit unterziehen möchten, oder es lieber in etwas bewegterem Wasser mögen- beim Stehpaddeln ist jeder richtig!</p>
    </div>
  </article>
</section>

</body>
</html>
```